Bookmark Design

We would like to design a book mark with logos of our two business and a quote.

One side with the quote "The first wealth is health" - Tobias Quill Harrow and the two logos.

The back side has the two logos with its respective phone numbers and a common address (this is to be advised to the winner of the project).

```html
<!DOCTYPE html>
<html lang="en">
<head>
<meta charset="utf-8">
<title>Bookmark Design – Harbour Dental &amp; Brightvale Clinic</title>
<link href="https://fonts.googleapis.com/css2?family=Raleway:wght@300;800&family=Open+Sans:ital,wght@0,400;0,700;1,400&display=swap" rel="stylesheet">
<style>
  :root {
    --page-bg: #eaebec;
    --page-glow: #ffffff;
    --clinic-blue: #1f4fa0;
    --dental-green: #5fae55;
    --white: #ffffff;
    --label: #111111;
  }
  * { margin: 0; padding: 0; box-sizing: border-box; }
  html, body { width: 1200px; height: 1200px; overflow: hidden; }
  body {
    position: relative;
    background: radial-gradient(ellipse 55% 45% at 50% 50%, var(--page-glow), var(--page-bg));
    font-family: "Open Sans", sans-serif;
  }
  .side-label {
    position: absolute; left: 60px;
    font-family: "Open Sans", sans-serif; font-size: 40px; color: var(--label);
    line-height: 1;
  }
  .side-label--a { top: 70px; }
  .side-label--b { top: 620px; }

  .bookmark { position: absolute; width: 1080px; height: 360px; overflow: hidden; }
  .bookmark--front { left: 55px; top: 156px; }
  .bookmark--back { left: 52px; top: 680px; }
  .bookmark__bg { position: absolute; inset: 0; width: 100%; height: 100%; }

  .abs { position: absolute; color: var(--white); white-space: nowrap; line-height: 1; }

  .quote-lead { left: 187px; top: 110px; font-family: "Raleway", sans-serif; font-weight: 300; font-size: 50px; }
  .quote-word { font-family: "Raleway", sans-serif; font-weight: 800; font-size: 128px; letter-spacing: -2px; top: 132px; }
  .quote-word--wealth { left: 124px; }
  .quote-word--health { left: 612px; }
  .quote-joiner { left: 575px; top: 206px; font-family: "Raleway", sans-serif; font-weight: 300; font-size: 42px; }
  .quote-rule { position: absolute; left: 585px; top: 301px; width: 150px; height: 2px;
    background: linear-gradient(90deg, rgba(255,255,255,0), var(--white) 40%); }
  .quote-author { left: 736px; top: 280px; font-style: italic; font-size: 27px; }

  .brand {
    position: absolute; display: flex; flex-direction: column; align-items: center; gap: 6px;
    text-align: center; white-space: nowrap;
    font-family: "Open Sans", sans-serif; font-weight: 700; line-height: 1.1;
    transform: translateX(-50%);
  }
  .brand__dot { border-radius: 50%; flex: none; }
  .brand--clinic { color: var(--clinic-blue); }
  .brand--clinic .brand__dot { border: 3px solid var(--clinic-blue); }
  .brand--dental { color: var(--dental-green); }
  .brand--dental .brand__dot { background: var(--dental-green); }

  .bookmark--front .brand--clinic { left: 800px; top: 24px; font-size: 13px; }
  .bookmark--front .brand--dental { left: 932px; top: 24px; font-size: 14px; }
  .bookmark--front .brand__dot { width: 40px; height: 40px; }

  .bookmark--back .brand--dental { left: 468px; top: 70px; font-size: 17px; }
  .bookmark--back .brand--clinic { left: 444px; top: 222px; font-size: 15px; }
  .bookmark--back .brand__dot { width: 42px; height: 42px; }

  .phone { left: 125px; font-size: 29px; }
  .phone--dental { top: 132px; }
  .phone--clinic { top: 281px; }
  .address { left: 620px; top: 224px; font-style: italic; font-size: 28px; line-height: 36px; }
</style>
</head>
<body>
  <div class="side-label side-label--a">Side A</div>

  <section class="bookmark bookmark--front">
    <svg class="bookmark__bg" viewBox="0 0 1739 579" preserveAspectRatio="none" aria-hidden="true">
      <defs>
        <linearGradient id="frontViolet" x1="0" y1="1" x2="0.75" y2="0">
          <stop offset="0" stop-color="#00215a"/>
          <stop offset="1" stop-color="#625ca8"/>
        </linearGradient>
        <radialGradient id="frontGreen" cx="0.72" cy="0" r="1" gradientTransform="translate(0.72 0) scale(0.9 1.1) translate(-0.72 0)">
          <stop offset="0" stop-color="#f4fbf1"/>
          <stop offset="0.3" stop-color="#6db566"/>
          <stop offset="0.6" stop-color="#449a4f"/>
          <stop offset="1" stop-color="#08612b"/>
        </radialGradient>
      </defs>
      <rect width="1739" height="579" fill="url(#frontViolet)"/>
      <polygon points="961,0 998,0 864,579 846,579" fill="#ffffff" opacity="0.18"/>
      <polygon points="998,0 1739,0 1739,579 864,579" fill="url(#frontGreen)"/>
    </svg>

    <div class="brand brand--clinic"><span class="brand__dot"></span><span>BRIGHTVALE<br>CLINIC</span></div>
    <div class="brand brand--dental"><span class="brand__dot"></span><span>Harbour Dental<br>Brightvale</span></div>

    <p class="abs quote-lead">The first</p>
    <p class="abs quote-word quote-word--wealth">wealth</p>
    <p class="abs quote-joiner">is</p>
    <p class="abs quote-word quote-word--health">health</p>
    <span class="quote-rule"></span>
    <p class="abs quote-author">Tobias Quill Harrow</p>
  </section>

  <div class="side-label side-label--b">Side B</div>

  <section class="bookmark bookmark--back">
    <svg class="bookmark__bg" viewBox="0 0 1739 579" preserveAspectRatio="none" aria-hidden="true">
      <defs>
        <linearGradient id="backViolet" x1="0" y1="1" x2="0.6" y2="0">
          <stop offset="0" stop-color="#00215a"/>
          <stop offset="1" stop-color="#5a57a3"/>
        </linearGradient>
        <linearGradient id="backPanel" x1="0.2" y1="1" x2="0.7" y2="0">
          <stop offset="0" stop-color="#3d4a86"/>
          <stop offset="0.45" stop-color="#e2e1f0"/>
          <stop offset="1" stop-color="#9c98c9"/>
        </linearGradient>
        <radialGradient id="backGreen" cx="0.8" cy="0" r="1" gradientTransform="translate(0.8 0) scale(0.9 1.1) translate(-0.8 0)">
          <stop offset="0" stop-color="#f4fbf1"/>
          <stop offset="0.3" stop-color="#6db566"/>
          <stop offset="0.6" stop-color="#449a4f"/>
          <stop offset="1" stop-color="#08612b"/>
        </radialGradient>
      </defs>
      <rect width="1739" height="579" fill="url(#backViolet)"/>
      <polygon points="616,0 976,0 846,579 516,579" fill="url(#backPanel)"/>
      <polygon points="976,0 999,0 864,579 846,579" fill="#e6e5f2"/>
      <polygon points="999,0 1739,0 1739,579 864,579" fill="url(#backGreen)"/>
    </svg>

    <p class="abs phone phone--dental">+61 2345 6789</p>
    <p class="abs phone phone--clinic">+61 2345 6789</p>

    <div class="brand brand--dental"><span class="brand__dot"></span><span>Harbour Dental<br>Brightvale</span></div>
    <div class="brand brand--clinic"><span class="brand__dot"></span><span>BRIGHTVALE<br>CLINIC</span></div>

    <p class="abs address">42 Marlow Lane<br>KESTREL BAY QLD 4870</p>
  </section>
</body>
</html>
```